Bref créative
Trucking Company Business Cards Stationary
KVR Freight Solutions
Professional
Beto Quiroga
Terminal Manager
4100 Harborview Blvd
Crestmoor, TX 77400
kvrfreightsolutions@mailbox-example.com
i would like something similar to this on the back side of card
i would also like something similar to this on the back side of my card

```html
<!DOCTYPE html>
<html lang="en">
<head>
<meta charset="utf-8">
<title>KVR Freight Solutions – Business Card</title>
<link rel="stylesheet" href="https://fonts.googleapis.com/css2?family=Open+Sans:wght@400;600;700;800&display=swap">
<style>
  :root {
    --page-bg: #e9e7e4;
    --card-bg: #ffffff;
    --brand-red: #b3151c;
    --text-dark: #3a3a3a;
    --text-mid: #555555;
    --icon-bg: #b3151c;
    --icon-fg: #ffffff;
  }
  * { margin: 0; padding: 0; box-sizing: border-box; }
  html, body {
    width: 1200px; height: 902px; overflow: hidden;
    background: var(--page-bg);
    font-family: "Open Sans", Arial, sans-serif;
  }
  .business-card {
    position: absolute; left: 100px; top: 165px;
    width: 1000px; height: 572px;
    background: var(--card-bg);
    box-shadow: 0 10px 30px rgba(0,0,0,0.18);
  }
  .brand {
    position: absolute; top: 110px; left: 0; width: 100%;
    display: flex; justify-content: center; align-items: center; gap: 14px;
    color: var(--brand-red);
    font-weight: 800; font-size: 44px; letter-spacing: 0.5px;
  }
  .brand-dot {
    width: 26px; height: 26px; border-radius: 50%;
    background: var(--brand-red);
  }
  .identity {
    position: absolute; top: 300px; left: 0; width: 100%;
    text-align: center; font-size: 27px; color: var(--text-dark);
  }
  .identity .person-name { color: var(--brand-red); font-weight: 700; }
  .identity .divider { margin: 0 10px; color: var(--text-dark); }
  .contacts {
    position: absolute; left: 0; width: 100%;
    display: flex; justify-content: center; gap: 40px;
    font-size: 19px; color: var(--text-mid);
  }
  .contacts.row-one { top: 380px; }
  .contacts.row-two { top: 420px; }
  .contact-item { display: flex; align-items: center; gap: 8px; }
  .contact-icon {
    width: 22px; height: 22px; border-radius: 50%;
    background: var(--icon-bg);
    display: inline-flex; align-items: center; justify-content: center;
    flex-shrink: 0;
  }
  .contact-icon svg { width: 13px; height: 13px; fill: var(--icon-fg); stroke: var(--icon-fg); }
</style>
</head>
<body>
  <div class="business-card">
    <div class="brand">
      <span class="brand-dot"></span>
      <span class="brand-name">KVR Freight Solutions</span>
    </div>

    <div class="identity">
      <span class="person-name">Beto Quiroga</span><span class="divider">|</span><span class="person-title">Terminal Manager</span>
    </div>

    <div class="contacts row-one">
      <div class="contact-item">
        <span class="contact-icon">
          <svg viewBox="0 0 12 12"><path stroke="none" d="M6 0.5a4 4 0 0 0-4 4c0 3 4 7 4 7s4-4 4-7a4 4 0 0 0-4-4zm0 5.5a1.5 1.5 0 1 1 0-3 1.5 1.5 0 0 1 0 3z"/></svg>
        </span>
        <span>4100 Harborview Blvd Crestmoor, TX 77400</span>
      </div>
      <div class="contact-item">
        <span class="contact-icon">
          <svg viewBox="0 0 12 12"><g fill="none" stroke-width="1.1"><circle cx="6" cy="6" r="4.8"/><ellipse cx="6" cy="6" rx="2" ry="4.8"/><path d="M1.2 6h9.6"/></g></svg>
        </span>
        <span>www.kvrfreight-example.com</span>
      </div>
    </div>

    <div class="contacts row-two">
      <div class="contact-item">
        <span class="contact-icon">
          <svg viewBox="0 0 12 12"><path stroke="none" d="M2.5 1l2 2-1 1.5c.7 1.4 1.6 2.3 3 3L8 6.5l2 2-1.2 1.8C5 10 2 7 1.7 2.2z"/></svg>
        </span>
        <span>2815550142</span>
      </div>
      <div class="contact-item">
        <span class="contact-icon">
          <svg viewBox="0 0 12 12"><path stroke="none" d="M3.5 0.5h5a1 1 0 0 1 1 1v9a1 1 0 0 1-1 1h-5a1 1 0 0 1-1-1v-9a1 1 0 0 1 1-1zm0.5 1.5v7h4V2z"/></svg>
        </span>
        <span>2815550187</span>
      </div>
      <div class="contact-item">
        <span class="contact-icon">
          <svg viewBox="0 0 12 12"><path stroke="none" d="M1 2.5h10v7H1z"/><path fill="none" stroke="#b3151c" stroke-width="1" d="M1.3 2.8L6 6.5l4.7-3.7"/></svg>
        </span>
        <span>kvrfreightsolutions@mailbox-example.com</span>
      </div>
    </div>
  </div>
</body>
</html>
```